Welcome Card Banner Desing for email suscriptors

to get involved on this task please check my site tulavendo.app
I wish for this task a welcome postal card to get subscribers for the newsletter and get a Coupon Code for discounts,
Keep in mind Velisso is a platform where customers (girls) can get any fashion high-end accessories ready to wear, to see the categories please visit our shop.

Target Market(s)

World wide people between 18-60 years old

Industry/Entity Type

Fashion

Coding

Coded - Design and coding required

Number of Pages Required

1 page

Font styles to use
Sans Serif

Colors
a64599
ffffff
ffc214
faa54b

Requirements
Must have
• Simplicity
• to get involved on this task please check my site tulavendo.app
• I wish for this task a welcome postal card to get subscribers for the newsletter and get a Coupon Code for discounts,
• Keep in mind Velisso is a platform where customers (girls) can get any fashion high-end accessories ready to wear, to see the categories please visit our shop.
Nice to have
• Field for customer fill an email or just skip the banner
Should not have
• Bad grammar

```html
<!DOCTYPE html>
<html lang="en">
<head>
<meta charset="UTF-8">
<title>Welcome Postal Card – Newsletter</title>
<link rel="stylesheet" href="https://fonts.googleapis.com/css2?family=Poppins:wght@300;400;800;900&display=swap">
<style>
  :root {
    --stage: #4b4b4b;
    --card-light: #f1f1f0;
    --card-shade: #e2e2e0;
    --band-orange: #f0a92e;
    --band-fold: #d6d6d4;
    --brand-purple: #a64599;
    --brand-yellow: #ffc214;
    --ink: #1d1d1d;
    --white: #ffffff;
    --button-dark: #434343;
    --button-edge: #6a6a6a;
  }
  * { box-sizing: border-box; margin: 0; padding: 0; }
  html, body {
    width: 1200px; height: 1200px; overflow: hidden;
    background: var(--stage);
    font-family: "Poppins", sans-serif;
  }
  .postal-card {
    position: absolute; left: 0; top: 211px;
    width: 1200px; height: 777px;
    background: radial-gradient(ellipse at 40% 30%, var(--card-light) 0%, var(--card-shade) 100%);
    overflow: hidden;
  }
  .band-art { position: absolute; inset: 0; }
  .photo-circle {
    position: absolute; border-radius: 50%;
    border: 2px solid var(--brand-purple);
    padding: 8px; background: var(--white);
  }
  .photo-circle .photo-fill { width: 100%; height: 100%; border-radius: 50%; }
  .photo-model { left: 80px; top: 102px; width: 310px; height: 310px; }
  .photo-model .photo-fill { background: linear-gradient(180deg, #f0ece6 0%, #d9c8b0 45%, #2a2a2a 100%); }
  .photo-bags { left: 796px; top: 102px; width: 310px; height: 310px; }
  .photo-bags .photo-fill { background: radial-gradient(circle at 50% 60%, #e6c1bd 0%, #f4e7e5 45%, #ffffff 75%); }
  .welcome-badge {
    position: absolute; left: 408px; top: 20px; width: 372px; height: 372px;
    border-radius: 50%; border: 20px solid var(--brand-yellow);
    background: var(--white); padding: 10px;
  }
  .welcome-badge .photo-fill {
    width: 100%; height: 100%; border-radius: 50%;
    background: radial-gradient(circle at 50% 50%, #e9c978 0%, #f7ecd0 40%, #ffffff 72%);
  }
  .headline {
    position: absolute; left: 0; width: 1200px; top: 445px;
    display: flex; align-items: center; justify-content: center; gap: 14px;
    font-weight: 300; font-size: 53px; color: var(--ink); line-height: 1;
  }
  .headline .rule { display: flex; flex-direction: column; gap: 5px; }
  .headline .rule span { display: block; height: 3px; background: var(--white); }
  .rule-left span:nth-child(1) { width: 150px; }
  .rule-left span:nth-child(2) { width: 118px; margin-left: 32px; }
  .rule-left span:nth-child(3) { width: 150px; }
  .rule-right span:nth-child(1) { width: 150px; }
  .rule-right span:nth-child(2) { width: 118px; }
  .rule-right span:nth-child(3) { width: 150px; }
  .offer-line {
    position: absolute; left: 0; width: 1200px; text-align: center;
    font-weight: 800; font-size: 38px; line-height: 1; text-transform: uppercase;
    letter-spacing: -0.3px;
  }
  .offer-newsletter { top: 510px; color: var(--white); }
  .offer-coupon { top: 563px; color: var(--brand-purple); }
  .subscribe-button {
    position: absolute; left: 275px; top: 626px; width: 647px; height: 110px;
    background: var(--button-dark);
    border: 3px solid var(--button-dark);
    outline: 2px solid var(--button-edge); outline-offset: -9px;
    display: flex; align-items: center; justify-content: center; gap: 20px;
    color: var(--brand-yellow); font-weight: 900; font-size: 48px;
    text-transform: uppercase; text-decoration: none;
  }
  .subscribe-button svg { width: 38px; height: 44px; }
</style>
</head>
<body>
  <main class="postal-card">
    <svg class="band-art" viewBox="0 0 1200 777" aria-hidden="true">
      <polygon points="30,445 110,445 110,660 30,660 62,552" fill="var(--band-fold)"/>
      <polygon points="1170,445 1090,445 1090,660 1170,660 1138,552" fill="var(--band-fold)"/>
      <polygon points="64,425 1136,425 1108,533 1136,641 64,641 92,533" fill="var(--band-orange)"/>
    </svg>

    <div class="photo-circle photo-model">
      <div class="photo-fill" role="img" aria-label="Smiling woman in a wide-brim hat and black top wearing a long pendant necklace"></div>
    </div>
    <div class="welcome-badge">
      <div class="photo-fill" role="img" aria-label="Hand-lettered Welcome! with gold stars and a gold triangle"></div>
    </div>
    <div class="photo-circle photo-bags">
      <div class="photo-fill" role="img" aria-label="Blush pink tote bag and matching pouch with a silk scarf"></div>
    </div>

    <h1 class="headline">
      <span class="rule rule-left"><span></span><span></span><span></span></span>
      Welcome Postal Card
      <span class="rule rule-right"><span></span><span></span><span></span></span>
    </h1>
    <p class="offer-line offer-newsletter">To get subscribers for the newsletter</p>
    <p class="offer-line offer-coupon">And get a coupon code for discounts</p>

    <a class="subscribe-button" href="#">
      <svg viewBox="0 0 38 44" aria-hidden="true"><polygon points="0,0 38,22 0,44" fill="var(--brand-yellow)"/></svg>
      Subscribers Now
    </a>
  </main>
</body>
</html>
```